Trade show post card for sportfishing

I would like a double sided postcard used to be a larger more descriptive, eye catching, marketing tool to be used at trade show. I want the double sided postcard to be descriptive and eye catching for both avid fisherman and inviting enough not to scare away first timers looking to enjoy the experience.

Target Market(s)

Males 25-60

Colors

Designer to choose colors to be used in the design.

Requirements
Must have
• My logo, website, phone number, type of trips, pictures of fishing trips we have had which I included below. But I do not need all of the pictures designers can use ones they feel will be most appealing
Nice to have
• Color scheme that works with my logo.

```html
<!DOCTYPE html>
<html lang="en">
<head>
<meta charset="utf-8">
<title>Tight Line Charters – Trade Show Postcard</title>
<link rel="stylesheet" href="https://fonts.googleapis.com/css2?family=Lobster+Two:wght@400&family=Titillium+Web:wght@400;600;700&display=swap">
<style>
  :root {
    --bg: #d4d4d4;
    --card: #ffffff;
    --green: #6cbd45;
    --green-dark: #0fa14c;
    --ink: #1c1c1c;
    --ink-soft: #2f2f2f;
    --rule: #8a8a8a;
    --shadow-curve: #a9a9a9;
  }
  * { box-sizing: border-box; margin: 0; padding: 0; }
  html, body { width: 1200px; height: 2250px; overflow: hidden; background: var(--bg); }
  body { position: relative; font-family: "Titillium Web", Arial, sans-serif; color: var(--ink); }

  .postcard {
    position: absolute; left: 100px; width: 1000px; height: 773px;
    background: var(--card); overflow: hidden;
    box-shadow: 0 14px 30px rgba(0,0,0,.35);
  }
  .postcard--front { top: 240px; }
  .postcard--back { top: 1180px; }
  .postcard svg.art { position: absolute; inset: 0; width: 100%; height: 100%; }

  /* Front */
  .front-brand {
    position: absolute; left: 60px; top: 540px; width: 250px;
    font-weight: 700; font-size: 40px; line-height: 1.05; color: var(--ink);
  }
  .contact { position: absolute; display: flex; align-items: center; gap: 16px; font-weight: 700; color: var(--ink); }
  .contact svg { flex: none; }
  .front-phone { left: 340px; top: 570px; font-size: 46px; }
  .front-web { left: 340px; top: 665px; font-size: 28px; font-weight: 600; gap: 12px; }

  /* Back */
  .pricing { position: absolute; left: 0; top: 0; width: 420px; color: var(--ink-soft); }
  .pricing-title {
    font-family: "Lobster Two", Georgia, cursive; font-weight: 400;
    font-size: 32px; line-height: 1.2; color: var(--ink);
    padding: 40px 0 0 32px;
  }
  .trip { margin-top: 14px; }
  .trip:first-of-type { margin-top: 18px; }
  .trip-head {
    display: flex; justify-content: space-between; width: 395px;
    background: var(--green-dark); color: #fff; font-weight: 600; font-size: 20px;
    padding: 1px 18px 1px 32px; line-height: 1.35;
  }
  .trip-list { list-style: none; padding: 6px 0 0 32px; width: 390px; }
  .trip-list li {
    position: relative; padding-left: 26px; font-size: 18px; line-height: 1.2;
    margin-bottom: 5px; color: #f4fbef;
  }
  .trip-list li svg { position: absolute; left: 0; top: 3px; }
  .back-phone { left: 32px; top: 580px; font-size: 32px; color: #fff; gap: 12px; }
  .back-web { left: 32px; top: 632px; font-size: 17px; font-weight: 600; color: #fff; gap: 8px; }

  .back-brand {
    position: absolute; left: 552px; top: 48px; width: 200px;
    font-weight: 700; font-size: 30px; line-height: 1.05; color: var(--ink);
  }
  .stamp-box { position: absolute; left: 801px; top: 40px; width: 134px; height: 132px; border: 2px solid var(--ink-soft); }
  .address-line { position: absolute; left: 666px; width: 268px; height: 0; border-top: 1.5px solid var(--rule); }
</style>
</head>
<body>

  <!-- Front side -->
  <section class="postcard postcard--front">
    <svg class="art" viewBox="0 0 1000 773" preserveAspectRatio="none">
      <defs>
        <linearGradient id="photoTone" x1="0" y1="0" x2="1" y2="1">
          <stop offset="0" stop-color="#8d9590"/>
          <stop offset="0.45" stop-color="#c9cdcc"/>
          <stop offset="1" stop-color="#6e7570"/>
        </linearGradient>
      </defs>
      <rect class="trip-photo" x="0" y="0" width="1000" height="773" fill="url(#photoTone)"
            role="img" aria-label="Photo of anglers on a charter boat on the river holding striped bass catches"/>
      <path class="green-swoosh" d="M0 462 C 320 420, 700 480, 1000 650 V773 H0 Z" fill="var(--green)"/>
      <path class="white-panel" d="M0 478 C 320 438, 700 498, 1000 672 V773 H0 Z" fill="var(--card)"/>
      <path class="frame-line" d="M15 520 V750 H978 V712" fill="none" stroke="var(--green)" stroke-width="5"/>
    </svg>

    <div class="front-brand">Tight Line Charters</div>

    <div class="contact front-phone">
      <svg width="46" height="46" viewBox="0 0 24 24" aria-hidden="true">
        <circle cx="12" cy="12" r="10.5" fill="none" stroke="var(--ink)" stroke-width="2"/>
        <path d="M8.2 6.5l1.8-.4 1.2 2.6-1.2 1c.6 1.4 1.6 2.4 3 3l1-1.2 2.6 1.2-.4 1.8c-.2.6-.8 1-1.5.9-3.8-.5-6.7-3.4-7.3-7.2-.1-.7.2-1.5.8-1.7z" fill="var(--ink)"/>
      </svg>
      <span>555 201 4477</span>
    </div>
    <div class="contact front-web">
      <svg width="20" height="20" viewBox="0 0 24 24" aria-hidden="true">
        <circle cx="12" cy="12" r="10" fill="none" stroke="var(--ink)" stroke-width="2"/>
        <path d="M2 12h20M12 2c3 3 3 17 0 20M12 2c-3 3-3 17 0 20" fill="none" stroke="var(--ink)" stroke-width="1.6"/>
      </svg>
      <span>www.tightlinecharters.com</span>
    </div>
  </section>

  <!-- Back side -->
  <section class="postcard postcard--back">
    <svg class="art" viewBox="0 0 1000 773" preserveAspectRatio="none" aria-hidden="true">
      <path class="panel-shade" d="M0 0 H420 C 490 80, 515 250, 500 380 C 488 520, 448 610, 418 663 H0 Z" fill="var(--shadow-curve)"/>
      <path class="pricing-panel" d="M0 0 H405 C 470 80, 492 250, 480 380 C 470 520, 430 610, 400 663 H0 Z" fill="var(--green)"/>
      <path class="contact-strip" d="M0 553 H452 C 440 590, 420 630, 400 663 H0 Z" fill="var(--green-dark)"/>
    </svg>

    <div class="pricing">
      <h1 class="pricing-title">Hudson River Striped<br>Bass Spring 2018 Pricing</h1>

      <div class="trip">
        <div class="trip-head"><span>Sunrise or Sunset Trip</span><span>$500.00</span></div>
        <ul class="trip-list">
          <li><svg width="16" height="16" viewBox="0 0 16 16"><rect x="1" y="1" width="14" height="14" rx="3" fill="none" stroke="#fff" stroke-width="1.5"/><path d="M4 8l3 3 5-6" fill="none" stroke="#fff" stroke-width="1.8"/></svg>5 Hours</li>
          <li><svg width="16" height="16" viewBox="0 0 16 16"><rect x="1" y="1" width="14" height="14" rx="3" fill="none" stroke="#fff" stroke-width="1.5"/><path d="M4 8l3 3 5-6" fill="none" stroke="#fff" stroke-width="1.8"/></svg>1-4 Guests</li>
          <li><svg width="16" height="16" viewBox="0 0 16 16"><rect x="1" y="1" width="14" height="14" rx="3" fill="none" stroke="#fff" stroke-width="1.5"/><path d="M4 8l3 3 5-6" fill="none" stroke="#fff" stroke-width="1.8"/></svg>all live bait</li>
          <li><svg width="16" height="16" viewBox="0 0 16 16"><rect x="1" y="1" width="14" height="14" rx="3" fill="none" stroke="#fff" stroke-width="1.5"/><path d="M4 8l3 3 5-6" fill="none" stroke="#fff" stroke-width="1.8"/></svg>top of the line fishing<br>gear and electronics</li>
        </ul>
      </div>

      <div class="trip">
        <div class="trip-head"><span>Full Day Trip</span><span>$900.00</span></div>
        <ul class="trip-list">
          <li><svg width="16" height="16" viewBox="0 0 16 16"><rect x="1" y="1" width="14" height="14" rx="3" fill="none" stroke="#fff" stroke-width="1.5"/><path d="M4 8l3 3 5-6" fill="none" stroke="#fff" stroke-width="1.8"/></svg>8 Hours</li>
          <li><svg width="16" height="16" viewBox="0 0 16 16"><rect x="1" y="1" width="14" height="14" rx="3" fill="none" stroke="#fff" stroke-width="1.5"/><path d="M4 8l3 3 5-6" fill="none" stroke="#fff" stroke-width="1.8"/></svg>1-4 Guests</li>
          <li><svg width="16" height="16" viewBox="0 0 16 16"><rect x="1" y="1" width="14" height="14" rx="3" fill="none" stroke="#fff" stroke-width="1.5"/><path d="M4 8l3 3 5-6" fill="none" stroke="#fff" stroke-width="1.8"/></svg>Times selected by captain to provide<br>best opportunity to catch fish</li>
          <li><svg width="16" height="16" viewBox="0 0 16 16"><rect x="1" y="1" width="14" height="14" rx="3" fill="none" stroke="#fff" stroke-width="1.5"/><path d="M4 8l3 3 5-6" fill="none" stroke="#fff" stroke-width="1.8"/></svg>All live bait</li>
          <li><svg width="16" height="16" viewBox="0 0 16 16"><rect x="1" y="1" width="14" height="14" rx="3" fill="none" stroke="#fff" stroke-width="1.5"/><path d="M4 8l3 3 5-6" fill="none" stroke="#fff" stroke-width="1.8"/></svg>Top of the line fishing<br>gear and electronics</li>
        </ul>
      </div>
    </div>

    <div class="contact back-phone">
      <svg width="34" height="34" viewBox="0 0 24 24" aria-hidden="true">
        <circle cx="12" cy="12" r="10.5" fill="none" stroke="#fff" stroke-width="2"/>
        <path d="M8.2 6.5l1.8-.4 1.2 2.6-1.2 1c.6 1.4 1.6 2.4 3 3l1-1.2 2.6 1.2-.4 1.8c-.2.6-.8 1-1.5.9-3.8-.5-6.7-3.4-7.3-7.2-.1-.7.2-1.5.8-1.7z" fill="#fff"/>
      </svg>
      <span>555 201 4477</span>
    </div>
    <div class="contact back-web">
      <svg width="13" height="13" viewBox="0 0 24 24" aria-hidden="true">
        <circle cx="12" cy="12" r="10" fill="none" stroke="#fff" stroke-width="2"/>
        <path d="M2 12h20M12 2c3 3 3 17 0 20M12 2c-3 3-3 17 0 20" fill="none" stroke="#fff" stroke-width="1.6"/>
      </svg>
      <span>www.tightlinecharters.com</span>
    </div>

    <div class="back-brand">Tight Line Charters</div>
    <div class="stamp-box"></div>
    <div class="address-line" style="top:292px"></div>
    <div class="address-line" style="top:346px"></div>
    <div class="address-line" style="top:400px"></div>
    <div class="address-line" style="top:454px"></div>
  </section>

</body>
</html>
```